Hi,

I need an illustration of the passage in the bible John 8:11 wherein a woman caught in adultery was brought to Jesus by the Pharisees who wanted to stone the woman. What I want is a picture of the accusing crowd leaving, the woman feeling shamed but remorseful and Jesus with His arms reaching for the woman offering to help her get up.

It's going to be a poster and there's going to be a caption that says like this

"Where are those who condemn you?" She said, "No one, Lord." And Jesus said unto her "Neither do I condemn you"

Receive the gift of no condemnation and be empowered to sin no more

The Pharisees would stone her if they could, but they couldn't
Jesus could, but He wouldn't
Jesus came not to judge but to save
Have you received His forgiveness?

I would want the words to be in a format that could really grab the attention of anyone who would be looking at the poster. What I want is for people to realise that Jesus is a loving saviour. While the sin on the passage is about adultery, it could also apply to any sin. Satan is always accusing but if we know and believe that all our sins have been paid for/forgiven instead of beating ourselves it's easy to move on. It's not because God has gone soft on sins but because Jesus has already paid everything in full.

I want the drawing and the words to really show the "style" of God's forgiveness, so loving, gracious and willing to forgive us without any requirements on our part except to receive gladly and rest in His loving arms, in the embrace of the Father.

I want the words to stand out and the drawing/sketch to highlight what the words are saying

Thanks

I have edited my brief, please check it out.

Thanks

I want the words to stand out more than the drawing/illustration.  The illustration is mainly to emphasise the message/word.

I'm thinking if the illustration/drawing can be a silhouette, would it be better?

Reason: Other designers have expressed intent to submit a design but haven't done it yet, so I thought it would be good to extend the deadline especially because I would think there have been a lot of projects submitted recently to take advantage of the discount recently offered.

Someone who would appreciate a christian message but not religious. Someone who would appreciate an artwork that is different, an artwork that would lighten up a room with it's design , colour, presentation and the message that goes with it.

Crowd

• An artwork that is "easy on the eye" and would lighten up a heavy heart or an artwork that has a "feel good" effect

A modern "decor" with a christian "message".

If the caption is too long maybe changed it to
And Jesus said "Neither do I condemn you" "Receive the gift of no condemnation and sin no more"

Jesus came not to condemn but to save

Would you let Him be your Saviour?
• www.brightpanelhouse.com.au and vorna.com.au have designs that are really nice, the designs are "light" and the colours are bright.

Later on I want other posters for other verses and I want to be able to put them together to make up a big poster.
• I don't want it to have the religious theme/feel

```html
<!DOCTYPE html>
<html lang="en">
<head>
<meta charset="utf-8">
<title>Neither Do I Condemn You — Poster</title>
<link rel="stylesheet" href="https://fonts.googleapis.com/css2?family=Righteous&family=Libre+Baskerville:ital,wght@0,400;0,700;1,700&family=Archivo+Black&family=Didact+Gothic&family=Lato:wght@300;400;700&family=Homemade+Apple&family=Cinzel:wght@700&display=swap">
<style>
  :root {
    --paper: #f2b45e;
    --paper-light: #f6c77c;
    --paper-deep: #e5a04a;
    --figure-light: #e9b066;
    --figure-dark: #b98543;
    --ink: #111111;
    --label: #ffffff;
  }
  * { margin: 0; padding: 0; box-sizing: border-box; }
  html, body { width: 776px; height: 1200px; overflow: hidden; }
  body { background: var(--paper); }

  .poster {
    position: relative;
    width: 776px;
    height: 1200px;
    overflow: hidden;
    background: radial-gradient(ellipse at 50% 30%, var(--paper-light), var(--paper) 60%, var(--paper-deep));
    color: var(--ink);
  }

  .scene-art {
    position: absolute;
    left: 0; top: 690px;
    width: 776px; height: 510px;
    background:
      radial-gradient(ellipse 230px 420px at 150px 340px, rgba(185,133,67,.55), transparent 70%),
      radial-gradient(ellipse 120px 300px at 760px 360px, rgba(150,105,50,.55), transparent 70%);
  }

  .strip { position: absolute; background: var(--label); }
  .strip--where { left: 54px; top: 64px; width: 456px; height: 122px; }
  .strip--edge { left: 679px; top: 64px; width: 97px; height: 127px; }
  .strip--bar-left { left: 184px; top: 316px; width: 12px; height: 118px; }
  .strip--bar-right { left: 564px; top: 316px; width: 12px; height: 118px; }
  .strip--pharisees { left: 0; top: 637px; width: 776px; height: 68px; }
  .strip--pharisees-tail { left: 0; top: 700px; width: 428px; height: 26px; }

  .headline-where {
    position: absolute; left: 60px; top: 68px;
    font-family: "Righteous", sans-serif;
    font-size: 112px; line-height: 1; letter-spacing: -2px;
  }
  .headline-rest {
    position: absolute; left: 518px; top: 72px;
    font-family: "Libre Baskerville", serif; font-weight: 700;
    font-size: 50px; line-height: 52px;
  }
  .headline-tail {
    position: absolute; left: 165px; top: 196px;
    font-family: "Libre Baskerville", serif; font-weight: 700;
    font-size: 40px;
  }
  .reply {
    position: absolute; left: 132px; top: 258px;
    font-family: "Libre Baskerville", serif; font-style: italic; font-weight: 700;
    font-size: 29px; letter-spacing: 1px;
  }
  .answer {
    position: absolute; left: 230px; top: 318px; width: 300px;
    font-family: "Archivo Black", sans-serif;
    font-size: 28px; line-height: 31px; text-align: right;
  }

  .gift {
    position: absolute; left: 41px; top: 480px; width: 701px; height: 98px;
    background: var(--label);
    font-family: "Didact Gothic", sans-serif;
    font-size: 31px; line-height: 39px; letter-spacing: 1px;
    text-align: center; padding-top: 10px;
  }

  .pharisees {
    position: absolute; right: 14px; top: 656px;
    font-family: "Lato", sans-serif; font-weight: 400; font-size: 25px;
  }
  .couldnt {
    position: absolute; right: 26px; top: 716px;
    font-family: "Homemade Apple", cursive; font-size: 12px; letter-spacing: 3px;
  }
  .would {
    position: absolute; left: 259px; top: 740px; width: 517px; height: 88px;
    background: var(--label);
    font-family: "Lato", sans-serif; font-size: 24px;
    text-align: right; padding: 26px 16px 0 0;
  }
  .would strong { font-weight: 700; font-size: 27px; }

  .save {
    position: absolute; left: 127px; top: 892px; width: 649px; height: 127px;
    background: var(--label);
    text-align: right; padding: 12px 12px 0 0;
  }
  .save__lead { font-family: "Lato", sans-serif; font-weight: 300; font-size: 37px; line-height: 46px; }
  .save__punch { font-family: "Cinzel", serif; font-weight: 700; font-size: 46px; line-height: 56px; letter-spacing: 2px; }

  .question {
    position: absolute; left: 452px; top: 1053px; width: 324px; height: 84px;
    background: var(--label);
    font-family: "Libre Baskerville", serif; font-size: 22px; line-height: 30px;
    text-align: right; padding: 12px 14px 0 0;
  }
</style>
</head>
<body>
<main class="poster">
  <div class="scene-art" role="img" aria-label="Faded silhouette illustration of Jesus reaching out to the woman as the crowd leaves"></div>

  <div class="strip strip--where"></div>
  <div class="strip strip--edge"></div>
  <div class="strip strip--bar-left"></div>
  <div class="strip strip--bar-right"></div>
  <div class="strip strip--pharisees"></div>
  <div class="strip strip--pharisees-tail"></div>

  <div class="headline-where">"WHERE</div>
  <div class="headline-rest">are<br>those</div>
  <div class="headline-tail">who condemn you?"</div>
  <div class="reply">She said, "No one, Lord."</div>
  <div class="answer">And Jesus said<br>unto her<br>"Neither do<br>I condemn you"</div>

  <p class="gift">Receive the gift of no condemnation<br>and be empowered to sin no more</p>

  <p class="pharisees">The Pharisees would stone her if they could,</p>
  <p class="couldnt">but they couldn't</p>
  <p class="would">Jesus could, <strong>but He wouldn't</strong></p>

  <div class="save">
    <p class="save__lead">Jesus came not to judge,</p>
    <p class="save__punch">BUT TO SAVE</p>
  </div>

  <p class="question">Have you received<br>His forgiveness?</p>
</main>
</body>
</html>
```